Corvath Properties Business Card Design

We would now like to design business cards with the new Corvath Properties logo

Target Market(s)

Professional

Industry/Entity Type

Professional services

Contact Information for Business Card

Employee name, title, phone number, email address, corporate office address and logo.

Font styles to use
Sans Serif

Colors
0054AA
0677BA
7BADD7
CADEEF
E8F1F8

Requirements
Must have
• My logo
Should not have
• any other pictures or images besides my logo

```html
<!DOCTYPE html>
<html lang="en">
<head>
<meta charset="utf-8">
<title>Corvath Properties Business Card</title>
<link rel="stylesheet" href="https://fonts.googleapis.com/css2?family=Arimo:wght@400;700&display=swap">
<style>
  :root {
    --page-bg: #e6e6e4;
    --card-white: #f6f6f6;
    --card-dark: #2a2b2e;
    --brand-blue: #0a78dc;
    --edge-blue: #0054aa;
    --ink: #2e2e2e;
    --rule: #3a3a3a;
    --card-shadow: rgba(0, 0, 0, 0.22);
  }
  * { box-sizing: border-box; margin: 0; padding: 0; }
  html, body {
    width: 1200px;
    height: 801px;
    overflow: hidden;
    background: var(--page-bg);
    font-family: "Arimo", Arial, sans-serif;
  }
  .stage {
    position: relative;
    width: 1200px;
    height: 801px;
  }
  .card {
    position: absolute;
    top: 246px;
    width: 540px;
    height: 309px;
    border-bottom: 4px solid var(--edge-blue);
    box-shadow: 0 14px 30px var(--card-shadow);
  }
  .card-front {
    left: 45px;
    background: var(--card-white);
  }
  .card-back {
    left: 615px;
    background: var(--card-dark);
  }

  /* Front */
  .brand-mark {
    position: absolute;
    right: 40px;
    top: 34px;
    display: flex;
    align-items: center;
    gap: 12px;
    color: var(--brand-blue);
    font-weight: 700;
    font-size: 26px;
    letter-spacing: 0.5px;
    text-transform: uppercase;
  }
  .brand-square {
    width: 34px;
    height: 34px;
    background: var(--brand-blue);
  }
  .divider {
    position: absolute;
    left: 40px;
    right: 40px;
    top: 170px;
    height: 1px;
    background: var(--rule);
  }
  .person {
    position: absolute;
    left: 40px;
    bottom: 150px;
  }
  .person-name {
    color: var(--brand-blue);
    font-weight: 700;
    font-size: 22px;
  }
  .person-title {
    color: var(--ink);
    font-size: 15px;
    margin-top: 3px;
  }
  .contacts {
    position: absolute;
    left: 40px;
    top: 186px;
    list-style: none;
    color: var(--ink);
    font-size: 15px;
    line-height: 26px;
  }
  .contacts li {
    display: flex;
    align-items: center;
    gap: 10px;
  }
  .contacts svg {
    width: 14px;
    height: 14px;
    fill: var(--brand-blue);
  }
  .address {
    position: absolute;
    right: 40px;
    top: 190px;
    text-align: right;
    color: var(--ink);
    font-size: 14px;
    font-style: normal;
    line-height: 19px;
  }

  /* Back */
  .back-name {
    position: absolute;
    right: 44px;
    top: 50%;
    transform: translateY(-50%);
    color: var(--brand-blue);
    font-weight: 700;
    font-size: 44px;
    line-height: 1.05;
    text-transform: uppercase;
    text-align: left;
  }
</style>
</head>
<body>
<main class="stage">

  <section class="card card-front" aria-label="Business card front">
    <div class="brand-mark">
      <span class="brand-square" aria-hidden="true"></span>
      <span class="brand-name">Corvath Properties</span>
    </div>

    <div class="person">
      <p class="person-name">Daniel Rourke</p>
      <p class="person-title">Manager</p>
    </div>

    <div class="divider" aria-hidden="true"></div>

    <ul class="contacts">
      <li>
        <svg viewBox="0 0 16 16" aria-hidden="true"><path d="M3.5 1.5l2.5 0 1.2 3.3-1.7 1.2c.8 1.7 2 2.9 3.7 3.7l1.2-1.7 3.3 1.2v2.5c0 .8-.7 1.5-1.5 1.5C6.7 13.2 2.8 9.3 2 3c0-.8.7-1.5 1.5-1.5z"/></svg>
        <span>555-318-2047</span>
      </li>
      <li>
        <svg viewBox="0 0 16 16" aria-hidden="true"><path d="M1 3h14v10H1z M2.2 4.2 8 8.6l5.8-4.4z" fill-rule="evenodd"/></svg>
        <span>d.rourke@corvathmail.com</span>
      </li>
      <li>
        <svg viewBox="0 0 16 16" aria-hidden="true"><path d="M8 1a7 7 0 1 0 0 14A7 7 0 0 0 8 1zm0 1.6c.9 0 1.9 1.9 2.1 4.6H5.9C6.1 4.5 7.1 2.6 8 2.6zM2.7 8.8h2.1c.1 1.6.5 3 1 4a5.4 5.4 0 0 1-3.1-4zm0-1.6a5.4 5.4 0 0 1 3.1-4c-.5 1-.9 2.4-1 4zm5.3 6.2c-.9 0-1.9-1.9-2.1-4.6h4.2c-.2 2.7-1.2 4.6-2.1 4.6zm2.2-.6c.5-1 .9-2.4 1-4h2.1a5.4 5.4 0 0 1-3.1 4zm1-5.6c-.1-1.6-.5-3-1-4a5.4 5.4 0 0 1 3.1 4z"/></svg>
        <span>www.corvathprops.com</span>
      </li>
    </ul>

    <address class="address">
      418 Harlow St, Dunmere<br>
      OR, ZIP 97310
    </address>
  </section>

  <section class="card card-back" aria-label="Business card back">
    <p class="back-name">Corvath<br>Properties</p>
  </section>

</main>
</body>
</html>
```